marlow keyhaven.com

we are a new company that offer people that have lost there bit coin transaction a recovery and retrieval service
We are looking for a website that will allow you to fill in your details

name
email
bitcoins or other crypto lost and date of transaction

and then an auto reply to them from a given email to verify there email

I am looking for an easy for the client to leave there interest and has a security look around it and looks familiar to the user.

https://tandrelpath.info/?gclid=Xq7LmPzTgRWbNcEvHsKyDa3UjFoeIq92hQ4nBvtzYc5rWpLm8-k2-fAdGxuoTjQe_NsVbHwMzYqEcPlKrUsDa_qwXz

https://osmerlinkgroup.com

https://www.frendaxo.com/faq-items/restoring-your-account-access/

Target Market(s)

early investors into crypto

Industry/Entity Type

It Company

Logo Text

MARLOW KEYHAVEN/FINDERS

Coding

Coded - Design and coding required

Number of Pages Required

3 page

Requirements
Must have
• be able to :
• complete
• Name,
• Email
• transaction date of exchange and how much they invested

```html
<!DOCTYPE html>
<html lang="en">
<head>
<meta charset="utf-8">
<title>Marlow Keyhaven – Finders</title>
<link href="https://fonts.googleapis.com/css2?family=Lato:wght@400;700;900&family=Open+Sans:wght@400;600;700&display=swap" rel="stylesheet">
<style>
:root{
  --orange:#f39a14;
  --orange-dark:#e58b05;
  --ink:#1f1f1f;
  --text:#555555;
  --muted:#8a8a8a;
  --band:#ececee;
  --footer:#1d1d1d;
  --line:#dcdcdc;
  --white:#ffffff;
}
*{box-sizing:border-box;margin:0;padding:0}
html,body{width:1200px;height:2497px;overflow:hidden}
body{position:relative;background:var(--white);font-family:"Open Sans",Arial,sans-serif;color:var(--text)}
.abs{position:absolute}
a{color:inherit;text-decoration:none}

/* top bar */
.topbar{left:0;top:0;width:1200px;height:34px;background:var(--orange);color:var(--white);font-size:11px}
.topbar .item{position:absolute;top:0;height:34px;display:flex;align-items:center;gap:7px}
.topbar .sep{position:absolute;top:11px;width:1px;height:12px;background:rgba(255,255,255,.7)}
.live-chat{left:1003px;width:97px;background:#2a2a2a;justify-content:center;font-weight:700}

/* hero */
.hero{left:0;top:34px;width:1200px;height:577px;
  background:
   radial-gradient(circle at 270px 240px,#d9a954 0,#b7893b 110px,#8c6a34 190px,rgba(180,170,170,0) 250px),
   radial-gradient(ellipse at 820px 420px,#d3a65a 0,rgba(210,170,100,.5) 150px,rgba(210,210,215,0) 300px),
   linear-gradient(180deg,#e9e9ee 0%,#dedfe4 55%,#c9c9cf 100%);}
.brand{left:98px;top:63px;display:flex;align-items:center;gap:12px}
.brand-dot{width:46px;height:46px;border-radius:50%;border:3px solid var(--orange)}
.brand-name{font-family:"Lato",sans-serif;font-weight:900;font-size:25px;color:var(--ink);letter-spacing:.3px}
.nav{top:67px;left:569px;height:34px;display:flex;align-items:center;font-size:13.5px;font-weight:600;color:#2b2b2b}
.nav a{margin-right:0}
.nav .active{background:var(--orange);color:var(--white);padding:0 19px;height:34px;display:flex;align-items:center;margin-right:26px}
.hero-title{left:672px;top:248px;font-family:"Lato",sans-serif;font-weight:900;font-size:45px;color:var(--ink);letter-spacing:.5px}
.hero-title span{color:var(--orange)}
.hero-sub{left:672px;top:318px;width:440px;font-family:"Lato",sans-serif;font-weight:700;font-size:17px;line-height:28px;color:#1e1e1e}
.btn-orange{background:var(--orange);color:var(--white);border-radius:24px;font-family:"Lato",sans-serif;font-weight:700;display:flex;align-items:center;justify-content:center}
.hero-btn{left:672px;top:404px;width:158px;height:45px;font-size:16px}
.slide-arrow{top:329px;width:40px;height:40px;border-radius:50%;background:rgba(120,120,120,.55);display:flex;align-items:center;justify-content:center}

/* news band */
.news{left:0;top:611px;width:1200px;height:184px;background:linear-gradient(120deg,#efeff1,#e6e6e9 50%,#f1f1f3)}
.date-ring{width:78px;height:78px;border-radius:50%;border:3px solid var(--orange);display:flex;flex-direction:column;align-items:center;justify-content:center;font-family:"Open Sans",sans-serif;color:var(--ink);background:var(--white);line-height:1}
.date-ring b{font-size:24px;font-weight:700}
.date-ring small{font-size:15px;font-weight:600;margin-top:3px}
.date-ring::before,.date-ring::after{content:"";position:absolute;width:8px;height:8px;border-radius:50%;background:var(--white);border:2px solid var(--orange);top:50%;margin-top:-4px}
.date-ring::before{left:-6px}.date-ring::after{right:-6px}
.news-title{left:223px;top:659px;font-size:15px;font-weight:700;color:var(--ink);letter-spacing:.3px}
.news-text{left:223px;top:695px;width:650px;font-size:12px;line-height:22px;color:var(--muted)}
.news-btn{left:935px;top:681px;width:165px;height:45px;font-size:14px}

/* recover */
.recover-title{left:98px;top:886px;font-family:"Lato",sans-serif;font-weight:700;font-size:31px;color:var(--ink)}
.recover-text{left:98px;top:958px;width:484px;font-size:12.5px;line-height:22px;text-align:justify;color:var(--text)}
.process-label{left:98px;top:1111px;font-size:19px;font-weight:600;color:var(--ink)}
.step{top:1171px;width:160px;text-align:center}
.step .date-ring{position:relative;margin:0 auto}
.step h4{margin-top:24px;font-size:17px;font-weight:700;color:var(--ink)}
.step p{margin-top:6px;font-size:13.5px;line-height:22px;color:var(--muted)}

/* contact */
.quick{left:646px;top:887px;width:454px;height:440px;background:var(--orange);color:var(--white)}
.quick h3{position:absolute;top:38px;width:100%;text-align:center;font-family:"Lato",sans-serif;font-size:30px;font-weight:700}
.quick .lead{position:absolute;top:92px;left:30px;width:394px;text-align:center;font-size:12.5px;line-height:23px}
.field{position:absolute;left:46px;width:361px;height:42px;border:1.5px solid rgba(255,255,255,.85);border-radius:4px;font-size:11.5px;padding:12px 18px}
.field.area{height:67px}
.submit{left:792px;top:1303px;width:162px;height:44px;border-radius:24px;background:#222;color:var(--white);font-family:"Lato",sans-serif;font-weight:700;font-size:16px;display:flex;align-items:center;justify-content:center}

.divider{left:98px;top:1441px;width:1002px;height:1px;background:var(--line)}

/* blog */
.blog-heading{left:0;top:1530px;width:1200px;text-align:center;font-family:"Lato",sans-serif;font-weight:700;font-size:31px;color:var(--ink)}
.card{top:1627px;width:311px}
.card .photo{height:217px;border:3px solid #eeeeee;border-radius:4px}
.card h4{margin-top:23px;font-size:19px;font-weight:600;color:var(--ink)}
.meta{margin-top:8px;display:flex;align-items:center;gap:8px;font-size:12.5px;color:#666}
.meta .bar{color:#999}
.excerpt{margin-top:14px;font-size:13px;line-height:22px;color:#777}
.more{margin-top:14px;display:flex;align-items:center;gap:7px;font-size:13px;font-weight:700;color:var(--orange)}

/* footer */
.footer{left:0;top:2113px;width:1200px;height:384px;background:var(--footer);color:var(--white)}
.f-brand{left:98px;top:2187px;display:flex;align-items:center;gap:12px}
.f-brand .brand-dot{width:40px;height:40px}
.f-brand span{font-family:"Lato",sans-serif;font-weight:700;font-size:20px;color:var(--white)}
.f-about{left:98px;top:2254px;width:266px;font-size:12px;line-height:23.5px;text-align:justify}
.f-col{top:2196px}
.f-col h5{font-size:16px;font-weight:700;letter-spacing:.5px;margin-bottom:22px}
.f-col li{list-style:none;font-size:12px;height:29px;display:flex;align-items:center;gap:9px}
.f-col li::before{content:"";width:5px;height:5px;border-top:2px solid var(--orange);border-right:2px solid var(--orange);transform:rotate(45deg)}
.socials{display:flex;gap:8px}
.socials span{width:29px;height:29px;border-radius:50%;border:1.5px solid var(--white)}
.f-line{left:98px;top:2406px;width:1002px;height:1px;background:#444}
.f-bottom{left:333px;top:2442px;font-size:13px;display:flex;gap:20px}
.to-top{left:1060px;top:2433px;width:37px;height:37px;border-radius:50%;background:var(--orange);display:flex;align-items:center;justify-content:center}
</style>
</head>
<body>

<!-- top bar -->
<div class="abs topbar">
  <div class="item" style="left:100px">
    <svg width="11" height="11" viewBox="0 0 24 24" fill="#fff"><path d="M6.6 10.8a15.1 15.1 0 0 0 6.6 6.6l2.2-2.2c.3-.3.7-.4 1-.2 1.1.4 2.3.6 3.6.6.6 0 1 .4 1 1V20c0 .6-.4 1-1 1C10.6 21 3 13.4 3 4c0-.6.4-1 1-1h3.5c.6 0 1 .4 1 1 0 1.3.2 2.5.6 3.6.1.3 0 .7-.2 1z"/></svg>
    (+1) 555 014 2290
  </div>
  <div class="sep" style="left:240px"></div>
  <div class="item" style="left:265px">
    <svg width="12" height="10" viewBox="0 0 24 18" fill="#fff"><path d="M0 0h24v2l-12 8L0 2zM0 4.5l12 8 12-8V18H0z"/></svg>
    info@marlowkeyhaven.com
  </div>
  <div class="item" style="left:835px">
    <svg width="9" height="11" viewBox="0 0 18 22" fill="#fff"><path d="M3 9V6a6 6 0 0 1 12 0v3h2v13H1V9zm3 0h6V6a3 3 0 0 0-6 0z"/></svg>
    LOGIN
  </div>
  <div class="sep" style="left:902px"></div>
  <div class="item" style="left:922px">
    <svg width="10" height="11" viewBox="0 0 20 22" fill="#fff"><circle cx="10" cy="6" r="5"/><path d="M0 22c0-6 4.5-9 10-9s10 3 10 9z"/></svg>
    SIGN UP
  </div>
  <div class="item live-chat">
    <svg width="12" height="11" viewBox="0 0 24 22" fill="#fff"><path d="M2 2h20v13H9l-5 5v-5H2z"/></svg>
    LIVE CHAT
  </div>
</div>

<!-- hero -->
<div class="abs hero" role="img" aria-label="Photograph of gold coins resting on a laptop keyboard with a market chart softly blurred behind"></div>
<div class="abs brand">
  <div class="brand-dot"></div>
  <div class="brand-name">MARLOW KEYHAVEN</div>
</div>
<nav class="abs nav">
  <a class="active" href="#">HOME</a>
  <a href="#" style="margin-right:26px">ABOUT</a>
  <a href="#" style="margin-right:26px">CARD</a>
  <a href="#" style="margin-right:26px">PRICING</a>
  <a href="#" style="margin-right:22px">BLOG</a>
  <a href="#" style="margin-right:22px">FAQ</a>
  <a href="#" style="margin-right:16px">CONTACT</a>
  <svg width="14" height="14" viewBox="0 0 24 24" fill="none" stroke="#2b2b2b" stroke-width="3"><circle cx="10" cy="10" r="7"/><path d="M15 15l7 7"/></svg>
</nav>
<h1 class="abs hero-title">MARLOW <span>KEYHAVEN</span></h1>
<p class="abs hero-sub">At vero eos et accusamus et iusto odio dignissimos ducimus qui blanditiis praesentium volupt.</p>
<a class="abs btn-orange hero-btn" href="#">READ MORE</a>
<div class="abs slide-arrow" style="left:17px"><svg width="12" height="14" viewBox="0 0 12 14"><path d="M9 1L3 7l6 6" fill="none" stroke="#fff" stroke-width="2.5"/></svg></div>
<div class="abs slide-arrow" style="left:1140px"><svg width="12" height="14" viewBox="0 0 12 14"><path d="M3 1l6 6-6 6" fill="none" stroke="#fff" stroke-width="2.5"/></svg></div>

<!-- news band -->
<div class="abs news"></div>
<div class="abs date-ring" style="left:102px;top:668px"><b>05</b><small>JAN</small></div>
<h2 class="abs news-title">PERFECTLY SIMPLE AND EASY TO DISTINGUISH</h2>
<p class="abs news-text">On the other hand, we denounce with righteous indignation and dislike men who are so beguiled and demoralized by the charms of pleasure of the moment, so blinded by desire, they cannot foresee the pain.</p>
<a class="abs btn-orange news-btn" href="#">VIEW ALL NEWS</a>

<!-- recover section -->
<h2 class="abs recover-title">How To Recover Your Bitcoin?</h2>
<p class="abs recover-text">At vero eos et accusamus et iusto odio dignissimos ducimus qui blanditiis praesentium voluptatum deleniti atque corrupti quos dolores et quas molestias excepturi sint occaecati cupiditate non provident, similique sunt in culpa qui officia deserunt mollitia animi, id est laborum et dolorum fuga. Et harum quidem rerum facilis est et expedita distinctio.</p>
<h3 class="abs process-label">Recovering Process:</h3>
<div class="abs step" style="left:86px">
  <div class="date-ring"><b>05</b><small>JAN</small></div>
  <h4>STEP 1</h4>
  <p>Dignissimos Ducimus<br>Praesentium</p>
</div>
<div class="abs step" style="left:261px">
  <div class="date-ring"><b>05</b><small>JAN</small></div>
  <h4>STEP 2</h4>
  <p>Dignissimos Ducimus<br>Praesentium</p>
</div>
<div class="abs step" style="left:436px">
  <div class="date-ring"><b>05</b><small>JAN</small></div>
  <h4>STEP 3</h4>
  <p>Dignissimos Ducimus<br>Praesentium</p>
</div>

<!-- quick contact -->
<form class="abs quick">
  <h3>Quick Contact</h3>
  <p class="lead">The initial consultation is free and you don't owe anything unless you get your coins back.</p>
  <div class="field" style="top:153px">Your Name</div>
  <div class="field" style="top:205px">Email Address</div>
  <div class="field" style="top:258px">Date of transaction</div>
  <div class="field area" style="top:311px">Which cryptocurrency are you trying to recover?</div>
</form>
<a class="abs submit" href="#">SUBMIT NOW</a>

<div class="abs divider"></div>

<!-- blog -->
<h2 class="abs blog-heading">Latest Blog Post</h2>
<article class="abs card" style="left:98px">
  <div class="photo" role="img" aria-label="Business illustration of glowing coins rising over a growth chart and world map" style="background:linear-gradient(135deg,#e9ecef,#c9ced3 45%,#f1d04a 60%,#8d939a)"></div>
  <h4>Foresee The Pain And Trouble</h4>
  <div class="meta"><svg width="12" height="12" viewBox="0 0 24 24" fill="#f39a14"><path d="M2 5h20v17H2zM6 1h3v5H6zm9 0h3v5h-3z"/><path d="M4 10h16v10H4z" fill="#fff"/></svg>02/01/2018<span class="bar">|</span><svg width="11" height="12" viewBox="0 0 20 22" fill="#f39a14"><circle cx="10" cy="6" r="5"/><path d="M0 22c0-6 4.5-9 10-9s10 3 10 9z"/></svg>Tessa Drummel</div>
  <p class="excerpt">Nam libero tempore, cum soluta nobis est eligendi optio cumque nihil impedit quo minus id</p>
  <a class="more" href="#">Read More <svg width="12" height="12" viewBox="0 0 24 24"><circle cx="12" cy="12" r="11" fill="#f39a14"/><path d="M10 7l5 5-5 5" stroke="#fff" stroke-width="3" fill="none"/></svg></a>
</article>
<article class="abs card" style="left:443px">
  <div class="photo" role="img" aria-label="Photograph of a gold coin in front of a glowing trading screen" style="background:radial-gradient(circle at 55% 60%,#d7a34a 0,#8a5a25 70px,rgba(30,40,70,0) 130px),linear-gradient(160deg,#1d2b4a,#3b3550 50%,#c86a2a)"></div>
  <h4>Foresee The Pain And Trouble</h4>
  <div class="meta"><svg width="12" height="12" viewBox="0 0 24 24" fill="#f39a14"><path d="M2 5h20v17H2zM6 1h3v5H6zm9 0h3v5h-3z"/><path d="M4 10h16v10H4z" fill="#fff"/></svg>02/01/2018<span class="bar">|</span><svg width="11" height="12" viewBox="0 0 20 22" fill="#f39a14"><circle cx="10" cy="6" r="5"/><path d="M0 22c0-6 4.5-9 10-9s10 3 10 9z"/></svg>Tessa Drummel</div>
  <p class="excerpt">Nam libero tempore, cum soluta nobis est eligendi optio cumque nihil impedit quo minus id</p>
  <a class="more" href="#">Read More <svg width="12" height="12" viewBox="0 0 24 24"><circle cx="12" cy="12" r="11" fill="#f39a14"/><path d="M10 7l5 5-5 5" stroke="#fff" stroke-width="3" fill="none"/></svg></a>
</article>
<article class="abs card" style="left:787px">
  <div class="photo" role="img" aria-label="Photograph of a smartphone on a laptop with glowing network lines" style="background:linear-gradient(150deg,#0f2f5a,#2a5d91 40%,#c7a45a 70%,#1b2437)"></div>
  <h4>Foresee The Pain And Trouble</h4>
  <div class="meta"><svg width="12" height="12" viewBox="0 0 24 24" fill="#f39a14"><path d="M2 5h20v17H2zM6 1h3v5H6zm9 0h3v5h-3z"/><path d="M4 10h16v10H4z" fill="#fff"/></svg>02/01/2018<span class="bar">|</span><svg width="11" height="12" viewBox="0 0 20 22" fill="#f39a14"><circle cx="10" cy="6" r="5"/><path d="M0 22c0-6 4.5-9 10-9s10 3 10 9z"/></svg>Tessa Drummel</div>
  <p class="excerpt">Nam libero tempore, cum soluta nobis est eligendi optio cumque nihil impedit quo minus id</p>
  <a class="more" href="#">Read More <svg width="12" height="12" viewBox="0 0 24 24"><circle cx="12" cy="12" r="11" fill="#f39a14"/><path d="M10 7l5 5-5 5" stroke="#fff" stroke-width="3" fill="none"/></svg></a>
</article>

<!-- footer -->
<footer class="abs footer"></footer>
<div class="abs f-brand"><div class="brand-dot"></div><span>MARLOW KEYHAVEN</span></div>
<p class="abs f-about">At vero eos et accusamus et iusto odio dignis simos ducimus qui blanditiis praesentium volup tatum deleniti atque corrupti quos do- lores et quas molestias excepturi sint.</p>
<div class="abs f-col" style="left:434px">
  <h5>SOLUTIONS</h5>
  <ul><li>Bitcoin Recovery</li><li>Retrieval Service</li><li>Bitcoin Wallet</li><li>Contact Us</li></ul>
</div>
<div class="abs f-col" style="left:624px">
  <h5>RESOURCES</h5>
  <ul><li>About Bitcoin</li><li>FAQ</li><li>Terms of Service</li><li>Privacy Policy</li></ul>
</div>
<div class="abs f-col" style="left:799px">
  <h5>COMPANY</h5>
  <ul><li>Support</li><li>Team</li><li>Careers</li><li>Press &amp; News</li></ul>
</div>
<div class="abs f-col" style="left:955px">
  <h5>FOLLOW US</h5>
  <div class="socials"><span></span><span></span><span></span><span></span></div>
</div>
<div class="abs f-line"></div>
<div class="abs f-bottom" style="color:#fff">
  <span>©2018 Marlow Keyhaven. All Rights Reserved.</span><span>|</span><span>Privacy Policy</span><span>|</span><span>Terms Of Use.</span>
</div>
<a class="abs to-top" href="#"><svg width="16" height="16" viewBox="0 0 24 24" fill="none" stroke="#fff" stroke-width="3"><path d="M5 13l7-7 7 7M5 20l7-7 7 7"/></svg></a>

</body>
</html>
```